Need a book cover design for a Lumora Book

Book has a long title and sub title so lots of words to fit on the cover.

I can be flexible a bit with the sub title due to the length of it but ideally i can get a design that takes everything.

Here is the title:

Tidal Geology: The Roots of Erosion, Sedimentation, and Canyon Forming

Sub Title/Heading
An Easy Primer on Coastal Cliffs, Dune Drift, River Beds, and Delta Mapping Methods

```html
<!DOCTYPE html>
<html lang="en">
<head>
<meta charset="utf-8">
<title>Tidal Geology — Book Cover</title>
<link rel="stylesheet" href="https://fonts.googleapis.com/css2?family=Poppins:wght@300;400;600;700;800&family=Josefin+Sans:wght@700&display=swap">
<style>
  :root {
    --page-bg: #f4f4f2;
    --cover-bg: #000000;
    --ink-white: #ffffff;
    --accent-red: #e0301a;
    --wave-deep: #3a0700;
    --wave-mid: #a3200c;
    --wave-glow: #f07a3a;
  }
  * { margin: 0; padding: 0; box-sizing: border-box; }
  html, body {
    width: 1200px;
    height: 2230px;
    overflow: hidden;
    background: var(--page-bg);
  }
  .book-cover {
    position: absolute;
    left: 40px;
    top: 220px;
    width: 1120px;
    height: 1790px;
    background: var(--cover-bg);
    color: var(--ink-white);
    font-family: "Poppins", sans-serif;
    text-align: center;
    overflow: hidden;
    box-shadow: 14px 16px 28px rgba(0, 0, 0, 0.35);
  }
  .title-top {
    position: absolute;
    top: 100px;
    left: 0;
    right: 0;
    font-weight: 400;
    font-size: 190px;
    line-height: 1;
    letter-spacing: -2px;
  }
  .title-main {
    position: absolute;
    top: 262px;
    left: 0;
    right: 0;
    font-weight: 700;
    font-size: 220px;
    line-height: 1;
    letter-spacing: -4px;
    color: var(--accent-red);
  }
  .subtitle {
    position: absolute;
    top: 520px;
    left: 0;
    right: 0;
    font-size: 58px;
    line-height: 1.12;
  }
  .subtitle-lead { font-weight: 300; display: block; font-size: 56px; }
  .subtitle-strong { font-weight: 800; display: block; letter-spacing: -0.5px; }
  .subtitle-strong .amp { font-weight: 400; }
  .wave-art {
    position: absolute;
    top: 760px;
    left: 0;
    width: 1120px;
    height: 640px;
  }
  .primer-label {
    position: absolute;
    top: 1418px;
    left: 0;
    right: 0;
    font-weight: 600;
    font-size: 40px;
    letter-spacing: 11px;
    color: var(--accent-red);
  }
  .primer-topics {
    position: absolute;
    top: 1478px;
    left: 0;
    right: 0;
    font-weight: 400;
    font-size: 35px;
    line-height: 1.12;
  }
  .author {
    position: absolute;
    top: 1622px;
    left: 0;
    right: 0;
    font-family: "Josefin Sans", sans-serif;
    font-weight: 700;
    font-size: 66px;
    letter-spacing: 14px;
  }
</style>
</head>
<body>
  <main class="book-cover">
    <h1>
      <span class="title-top">TIDAL</span>
      <span class="title-main">GEOLOGY</span>
    </h1>
    <p class="subtitle">
      <span class="subtitle-lead">THE ROOTS OF</span>
      <span class="subtitle-strong">EROSION, SEDIMENTATION,</span>
      <span class="subtitle-strong"><span class="amp">&amp;</span> CANYON FORMING</span>
    </p>
    <svg class="wave-art" role="img" aria-label="Glowing red and orange contour-line wave landscape of dotted particles" viewBox="0 0 1120 640">
      <defs>
        <radialGradient id="waveGlow" cx="0.55" cy="0.48" r="0.6">
          <stop offset="0" stop-color="var(--wave-glow)"/>
          <stop offset="0.3" stop-color="var(--wave-mid)"/>
          <stop offset="0.7" stop-color="var(--wave-deep)"/>
          <stop offset="1" stop-color="var(--cover-bg)"/>
        </radialGradient>
      </defs>
      <rect width="1120" height="640" fill="url(#waveGlow)"/>
    </svg>
    <p class="primer-label">AN EASY PRIMER ON</p>
    <p class="primer-topics">Coastal Cliffs, Dune Drift, River Beds,<br>and Delta Mapping Methods</p>
    <p class="author">OWEN CASTELL</p>
  </main>
</body>
</html>
```